Business Stationary, Letterhead, Fax Cover Sheet, Client Intake, Email Signature, Thank you cards.
Marwick Law Firm
Business Stationary, Letterhead, Fax Cover Sheet, Client Intake, Email Signature, Thank you cards. - Law
Creative Brief
Professional
Len Marwick
Lawyer
2837 Falbrook St., Suite 1940 Houston, Texas 77014
len@marwick-law.example
www.marwick-law.example
Please note this project is Not for just One Person but for All Staff. The files should be in editable format to allow for different names and titles on cards.

```html
<!DOCTYPE html>
<html lang="en">
<head>
<meta charset="utf-8">
<title>Marwick Law Firm Stationery</title>
<link rel="stylesheet" href="https://fonts.googleapis.com/css2?family=Arimo:wght@400;700&display=swap">
<style>
  :root {
    --bg: #e8e5e0;
    --paper: #ffffff;
    --navy: #1b2a8c;
    --blue: #2436d6;
    --deep: #0b1060;
    --ink: #333a4a;
    --rule: #c9ccd6;
    --card-dark: #0c0c10;
  }
  * { box-sizing: border-box; margin: 0; padding: 0; }
  html, body { width: 1200px; height: 734px; overflow: hidden; }
  body { background: var(--bg); font-family: "Arimo", Arial, sans-serif; color: var(--ink); position: relative; }

  .sheet { position: absolute; background: var(--paper); box-shadow: 0 3px 12px rgba(0,0,0,.18); }
  .band { position: absolute; left: 0; right: 0; bottom: 0; background: linear-gradient(90deg, var(--deep), var(--blue) 45%, var(--deep)); border-top: 3px solid #111; color: #dfe3ff; font-size: 8px; letter-spacing: .5px; display: flex; align-items: center; justify-content: center; }

  .brand { display: flex; align-items: center; gap: 6px; }
  .brand-dot { width: 16px; height: 16px; border-radius: 50%; background: var(--blue); flex: none; }
  .brand-name { font-weight: 700; color: var(--navy); font-size: 20px; letter-spacing: 1px; line-height: 1; }
  .tagline { font-size: 6px; color: var(--navy); letter-spacing: 1px; text-transform: uppercase; margin-top: 3px; }
  .address { font-size: 6.5px; line-height: 1.45; color: #555; margin-top: 5px; }

  /* Fax cover sheet */
  .fax { left: 132px; top: 108px; width: 288px; height: 540px; }
  .fax .head { position: absolute; left: 24px; top: 22px; }
  .fax .form { position: absolute; left: 22px; top: 110px; right: 22px; height: 380px; border: 1px solid var(--rule); border-radius: 6px; padding: 8px 10px; }
  .field { font-size: 7px; border-bottom: 1px solid var(--rule); height: 20px; display: flex; align-items: flex-end; padding-bottom: 3px; }
  .checks { display: flex; gap: 10px; font-size: 7px; margin: 10px 0 8px; }
  .checks span::before { content: ""; display: inline-block; width: 7px; height: 7px; border: 1px solid #777; margin-right: 3px; vertical-align: -1px; }
  .comments-label { font-size: 7px; margin-bottom: 2px; }
  .line { border-bottom: 1px solid var(--rule); height: 16px; }
  .fax .band { height: 16px; }

  /* Letterhead */
  .letterhead { left: 336px; top: 96px; width: 360px; height: 557px; }
  .letterhead .head { position: absolute; left: 30px; top: 26px; }
  .letterhead .band { height: 18px; }

  /* Envelope */
  .envelope { left: 688px; top: 108px; width: 370px; height: 228px; }
  .envelope .flap { position: absolute; left: 0; top: 0; width: 100%; height: 90px; }
  .envelope .head { position: absolute; left: 22px; top: 96px; }
  .envelope .band { height: 14px; }

  /* Business cards */
  .card { position: absolute; top: 372px; width: 176px; height: 108px; border-radius: 3px; box-shadow: 0 3px 10px rgba(0,0,0,.25); overflow: hidden; }
  .card-light { left: 688px; background: linear-gradient(160deg, #fff, #e6e7ec); }
  .card-dark { left: 882px; background: var(--card-dark); }
  .card .contact { position: absolute; right: 14px; top: 12px; font-size: 6px; line-height: 1.5; width: 74px; }
  .card .contact b { font-size: 7.5px; display: block; }
  .card .brand { position: absolute; left: 12px; bottom: 24px; }
  .card .brand-name { font-size: 13px; }
  .card .brand-dot { width: 10px; height: 10px; }
  .card .band { height: 12px; font-size: 6px; }
  .card-dark .contact { color: #d6d8e6; }
  .card-dark .brand-name { color: #6f86ff; }
</style>
</head>
<body>

<section class="sheet fax" aria-label="Fax cover sheet">
  <div class="head">
    <div class="brand"><span class="brand-dot"></span><span class="brand-name">MARWICK</span></div>
    <div class="tagline">Trial Lawyers Serving Houston</div>
    <div class="address">2837 Falbrook St., Suite 1940<br>Houston, Texas 77014<br>www.marwick-law.example</div>
  </div>
  <div class="form">
    <div class="field">To:</div>
    <div class="field">Fax:</div>
    <div class="field">Phone:</div>
    <div class="field">Re:</div>
    <div class="checks"><span>Urgent</span><span>For Review</span><span>Please Comment</span></div>
    <div class="comments-label">Comments:</div>
    <div class="line"></div><div class="line"></div><div class="line"></div><div class="line"></div>
    <div class="line"></div><div class="line"></div><div class="line"></div><div class="line"></div>
    <div class="line"></div><div class="line"></div><div class="line"></div><div class="line"></div>
  </div>
  <div class="band">www.marwick-law.example</div>
</section>

<section class="sheet letterhead" aria-label="Letterhead">
  <div class="head">
    <div class="brand"><span class="brand-dot"></span><span class="brand-name">MARWICK</span></div>
    <div class="tagline">Trial Lawyers Serving Houston</div>
    <div class="address">2837 Falbrook St., Suite 1940<br>Houston, Texas 77014</div>
  </div>
  <div class="band">www.marwick-law.example</div>
</section>

<section class="sheet envelope" aria-label="Envelope">
  <svg class="flap" viewBox="0 0 370 90" preserveAspectRatio="none">
    <polyline points="0,0 185,86 370,0" fill="none" stroke="#d3d5dc" stroke-width="1"/>
  </svg>
  <div class="head">
    <div class="brand"><span class="brand-dot"></span><span class="brand-name">MARWICK</span></div>
    <div class="address">2837 Falbrook St., Suite 1940<br>Houston, Texas 77014</div>
  </div>
  <div class="band"></div>
</section>

<section class="card card-light" aria-label="Business card, light">
  <div class="contact"><b>Len Marwick</b>Lawyer<br>2837 Falbrook St., Suite 1940<br>Houston, Texas 77014<br>len@marwick-law.example</div>
  <div class="brand"><span class="brand-dot"></span><span class="brand-name">MARWICK</span></div>
  <div class="band">www.marwick-law.example</div>
</section>

<section class="card card-dark" aria-label="Business card, dark">
  <div class="contact"><b>Len Marwick</b>Lawyer<br>2837 Falbrook St., Suite 1940<br>Houston, Texas 77014<br>len@marwick-law.example</div>
  <div class="brand"><span class="brand-dot"></span><span class="brand-name">MARWICK</span></div>
  <div class="band">www.marwick-law.example</div>
</section>

</body>
</html>
```